Need Label for Our Jams Product

HI,

we have are launching a new brand in the premium foods category by the name of Vo-Marta. the logo has been designed and our first product is Premium 65% fruit Jams. we need a label for it now. can you help ?

our flavours are strawberry, apple, mango, blackberry, cherry, PineApple.

Please note that we need one design and then we will modify it according to the flavour. so you will need to make one flavour on a theme. and then we will apply the theme accordingly to the rest of the flavours.

Target Market(s)

Health concious people who donot want to use ordinary jams any further.

Industry/Entity Type

Product

Requirements
Must have
• the logo, not too big because we need the flavour name aswell on the front of the label.
also would appreciate a touch of fruit or similar
also please note that the colour of the cap in the attached picture is the actual colour. and the label should incline with the colour of cap aswell. im not saying the label to be in that colour, but must balance the whole look of the bottle.
Please note that this is a round bottle, so much information is needed on the front. the sides of the labels will be occupied by ingredients nutrition facts etc.
Nice to have
• white background but not necessary.
Should not have
• black colour

```html
<!DOCTYPE html>
<html lang="en">
<head>
<meta charset="utf-8">
<title>Vo-Marta Premium Blackberry Jam Label</title>
<link href="https://fonts.googleapis.com/css2?family=Cabin:ital,wght@0,600;1,700&family=PT+Sans:wght@400;700&display=swap" rel="stylesheet">
<style>
  :root {
    --page: #ffffff;
    --plum: #2b2158;
    --plum-soft: #6f67a2;
    --leaf: #6cbf2a;
    --cocoa: #6b5a48;
    --bronze: #7a3d12;
    --copper-dark: #5a2a0a;
    --copper: #d9801c;
    --gold: #f4c24a;
    --ink: #6b4a2a;
    --guide: #23d3e0;
    --rule: #111111;
    --copper-band: linear-gradient(90deg, var(--copper-dark) 0%, var(--copper) 18%, var(--gold) 30%, var(--copper) 45%, var(--copper-dark) 60%, var(--copper) 78%, var(--gold) 88%, var(--copper-dark) 100%);
  }
  * { box-sizing: border-box; margin: 0; padding: 0; }
  html, body { width: 1200px; height: 900px; overflow: hidden; background: var(--page); }
  .canvas { position: relative; width: 1200px; height: 900px; font-family: "PT Sans", sans-serif; }

  /* front panel */
  .front-panel { position: absolute; background: var(--plum); overflow: hidden; }
  .front-panel--large { left: 113px; top: 92px; width: 410px; height: 400px; }
  .front-panel--small { left: 484px; top: 645px; width: 209px; height: 205px; }
  .fruit-pattern {
    position: absolute; inset: 0;
    background: linear-gradient(135deg, var(--plum) 0%, var(--plum-soft) 30%, var(--plum) 50%, var(--plum-soft) 72%, var(--plum) 100%);
  }
  .brand-plate {
    position: absolute; background: #fff;
    display: flex; align-items: center; justify-content: center; gap: 8px;
  }
  .front-panel--large .brand-plate { left: 94px; top: 15px; width: 221px; height: 85px; }
  .front-panel--small .brand-plate { left: 48px; top: 8px; width: 112px; height: 43px; gap: 4px; }
  .brand-name { font-family: "PT Sans", sans-serif; font-weight: 400; color: var(--leaf); line-height: 1; }
  .front-panel--large .brand-name { font-size: 46px; }
  .front-panel--small .brand-name { font-size: 23px; }
  .brand-dot { border-radius: 50%; background: var(--leaf); }
  .front-panel--large .brand-dot { width: 12px; height: 12px; }
  .front-panel--small .brand-dot { width: 6px; height: 6px; }

  .flavour-plate { position: absolute; }
  .front-panel--large .flavour-plate { left: 124px; top: 213px; width: 162px; height: 76px; }
  .front-panel--small .flavour-plate { left: 63px; top: 105px; width: 82px; height: 39px; }
  .flavour-plate svg { position: absolute; inset: 0; width: 100%; height: 100%; }
  .flavour-name {
    position: absolute; inset: 0; display: flex; flex-direction: column; align-items: center; justify-content: center;
    font-family: "Cabin", sans-serif; font-style: italic; font-weight: 700; color: var(--cocoa); text-align: center; line-height: 1.12;
  }
  .front-panel--large .flavour-name { font-size: 19.5px; padding-top: 4px; }
  .front-panel--small .flavour-name { font-size: 10px; padding-top: 2px; }
  .fruit-content { position: absolute; width: 100%; text-align: center; color: #fff; font-weight: 700; }
  .front-panel--large .fruit-content { top: 293px; font-size: 17px; }
  .front-panel--small .fruit-content { top: 148px; font-size: 9px; }

  /* wrap label */
  .wrap-label { position: absolute; left: 113px; top: 645px; width: 1004px; height: 205px; border: 1px solid var(--guide); }
  .wrap-label__overlap { position: absolute; left: 952px; top: 0; width: 1px; height: 100%; background: var(--guide); }
  .copper-band { position: absolute; left: 0; width: 953px; height: 14px; background: var(--copper-band); }
  .copper-band--top { top: 0; }
  .copper-band--bottom { bottom: 0; height: 16px; }
  .side-copy {
    position: absolute; top: 36px;
    font-size: 11.1px; line-height: 12.7px; color: var(--ink);
  }
  .side-copy span { display: block; white-space: nowrap; }
  .side-copy--a { left: 22px; }
  .side-copy--b { left: 189px; }
  .side-copy--c { left: 598px; }
  .side-copy--d { left: 764px; }

  /* dimensions */
  .dimension { position: absolute; font-family: Arial, sans-serif; font-size: 13px; color: var(--rule); }
  .dimension svg { position: absolute; overflow: visible; }
  .dimension--width { left: 105px; top: 606px; width: 970px; height: 20px; }
  .dimension--width span { position: absolute; left: 452px; top: 0; background: var(--page); padding: 0 8px; }
  .dimension--height { left: 76px; top: 638px; width: 20px; height: 220px; }
  .dimension--height span { position: absolute; left: -16px; top: 98px; transform: rotate(-90deg); background: var(--page); padding: 0 6px; }
</style>
</head>
<body>
<main class="canvas">

  <section class="front-panel front-panel--large" aria-label="Front label">
    <div class="fruit-pattern" role="img" aria-label="White silhouettes of pineapples, cherries, apples, mangoes, strawberries and blackberries scattered over plum"></div>
    <div class="brand-plate"><span class="brand-name">Vo-Marta</span><span class="brand-dot"></span></div>
    <div class="flavour-plate">
      <svg viewBox="0 0 162 76" preserveAspectRatio="none" aria-hidden="true">
        <path d="M3 10 Q81 -2 159 10 L159 73 L3 73 Z" fill="#fff" stroke="#7a3d12" stroke-width="4"/>
      </svg>
      <p class="flavour-name"><span>Premium</span><span>Blackberry Jam</span></p>
    </div>
    <p class="fruit-content">65% Fruit</p>
  </section>

  <div class="dimension dimension--width">
    <svg width="970" height="20"><line x1="2" y1="9" x2="968" y2="9" stroke="#111" stroke-width="1.2"/><path d="M0 9 L12 4 L12 14 Z M970 9 L958 4 L958 14 Z" fill="#111"/></svg>
    <span>224mm</span>
  </div>
  <div class="dimension dimension--height">
    <svg width="20" height="220"><line x1="9" y1="2" x2="9" y2="218" stroke="#111" stroke-width="1.2"/><path d="M9 0 L4 12 L14 12 Z M9 220 L4 208 L14 208 Z" fill="#111"/></svg>
    <span>47.9mm</span>
  </div>

  <section class="wrap-label" aria-label="Full wrap label">
    <div class="copper-band copper-band--top"></div>
    <div class="copper-band copper-band--bottom"></div>
    <div class="wrap-label__overlap"></div>
    <p class="side-copy side-copy--a">
      <span>Sed tempus, nibh in malesuada</span>
      <span>posuere, enim tortor lacinia</span>
      <span>tortor, vitae interdum mauris</span>
      <span>diam sit amet est. Donec nec</span>
      <span>nulla mauris. Maecenas velit</span>
      <span>tellus, porttitor venenatis</span>
      <span>consectetur et, varius id dolor.</span>
      <span>Sed eget tortor eget nulla</span>
      <span>lobortis dignissim sed et tellus.</span>
      <span>Vestibulum aliquam, ipsum eu</span>
      <span>dictum fringilla, tellus purus</span>
    </p>
    <p class="side-copy side-copy--b">
      <span>malesuada magna, quis ullam-</span>
      <span>corper enim nulla non mi.</span>
      <span>Mauris tortor augue, consequat</span>
      <span>neque. Donec nec nulla mauris.</span>
      <span>Maecenas velit tellus, porttitor</span>
      <span>venenatis consectetur et, varius</span>
      <span>id dolor. Sed eget tortor eget</span>
      <span>nulla lobortis dignissim sed et</span>
      <span>tellus. Vestibulum aliquam,</span>
      <span>ipsum eu dictum &nbsp;purus ullam-</span>
      <span>corper enim nulla non mi.</span>
    </p>
    <p class="side-copy side-copy--c">
      <span>Premium 65% fruit Jams.</span>
      <span>Lorem ipsum dolor sit amet,</span>
      <span>consectetur adipiscing elit. Duis</span>
      <span>rutrum dignissim ligula</span>
      <span>malesuada lobortis. Integer eros</span>
      <span>dui, sollicitudin vel adipiscing</span>
      <span>vitae, semper in elit. Vivamus</span>
      <span>rhoncus nulla libero, at lobortis</span>
      <span>nibh. Mauris sit amet turpis in</span>
      <span>ante cursus adipiscing. Sed dui</span>
      <span>nulla, eleifend vel imperdiet eu,</span>
    </p>
    <p class="side-copy side-copy--d">
      <span>sollicitudin id quam. Duis</span>
      <span>rutrum dignissim ligula</span>
      <span>malesuada lobortis. Sed dui</span>
      <span>nulla, eleifend vel. Duis rutrum</span>
      <span>dignissim ligula malesuada</span>
      <span>lobortis. Integer eros dui,</span>
      <span>sollicitudin vel adipiscing vitae,</span>
      <span>semper in elit. Vivamus rhoncus</span>
      <span>nulla libero, at lobortis nibh.</span>
      <span>Mauris sit amet turpis in ante</span>
      <span>cursus adipiscing.</span>
    </p>
  </section>

  <section class="front-panel front-panel--small" aria-label="Front panel on wrap label">
    <div class="fruit-pattern" role="img" aria-label="White silhouettes of assorted fruits scattered over plum"></div>
    <div class="brand-plate"><span class="brand-name">Vo-Marta</span><span class="brand-dot"></span></div>
    <div class="flavour-plate">
      <svg viewBox="0 0 162 76" preserveAspectRatio="none" aria-hidden="true">
        <path d="M3 10 Q81 -2 159 10 L159 73 L3 73 Z" fill="#fff" stroke="#7a3d12" stroke-width="5"/>
      </svg>
      <p class="flavour-name"><span>Premium</span><span>Blackberry Jam</span></p>
    </div>
    <p class="fruit-content">65% Fruit</p>
  </section>

</main>
</body>
</html>
```